Silver Heron Holdings, LLC Business Card

We need a logo that will be embossed or printed in a singular light color for Business Cards. Would be interested in seeing a Cypress Tree graphic. Our company name is Silver Heron Holdings, LLC. Business Card layout and graphic should project imagine of confidence, integrity and strength.

```html
<!DOCTYPE html>
<html lang="en">
<head>
<meta charset="utf-8">
<title>Silver Heron Holdings, LLC — Business Card</title>
<link href="https://fonts.googleapis.com/css2?family=Arvo:wght@700&family=Noto+Serif:wght@700&family=Open+Sans:wght@400;700&display=swap" rel="stylesheet">
<style>
  :root {
    --backdrop: #e8e5e1;
    --card: #111111;
    --mark-tone: #070707;
    --name-tone: #8c8c8c;
    --detail-tone: #9a9a9a;
    --label-tone: #8a8a8a;
  }
  * { margin: 0; padding: 0; box-sizing: border-box; }
  html, body {
    width: 1200px;
    height: 1000px;
    overflow: hidden;
    background: var(--backdrop);
  }
  .canvas {
    position: relative;
    width: 1200px;
    height: 1000px;
  }
  .card {
    position: absolute;
    width: 740px;
    height: 426px;
    background: var(--card);
  }
  .card--front { left: 387px; top: 53px; }
  .card--back  { left: 46px;  top: 503px; }

  .brand {
    position: absolute;
    left: 0;
    right: 0;
    top: 170px;
    display: flex;
    flex-direction: column;
    align-items: center;
    gap: 22px;
  }
  .brand__dot {
    width: 46px;
    height: 46px;
    border-radius: 50%;
    background: var(--mark-tone);
  }
  .brand__name {
    font-family: "Arvo", Georgia, serif;
    font-weight: 700;
    font-size: 28px;
    letter-spacing: 0.5px;
    color: var(--mark-tone);
  }

  .holder {
    position: absolute;
    left: 31px;
    top: 340px;
    text-align: right;
  }
  .holder__name {
    font-family: "Noto Serif", Georgia, serif;
    font-weight: 700;
    font-size: 27px;
    color: var(--name-tone);
    line-height: 1.1;
  }
  .holder__role {
    font-family: "Open Sans", Arial, sans-serif;
    font-size: 19px;
    color: var(--detail-tone);
    margin-top: 3px;
  }

  .contact {
    position: absolute;
    right: 31px;
    top: 342px;
    text-align: right;
    font-family: "Open Sans", Arial, sans-serif;
    font-size: 19.5px;
    color: var(--detail-tone);
    line-height: 35px;
  }
  .contact__label {
    font-weight: 700;
    color: var(--label-tone);
  }

  .website {
    position: absolute;
    left: 0;
    right: 0;
    top: 354px;
    text-align: center;
    font-family: "Open Sans", Arial, sans-serif;
    font-size: 22px;
    color: var(--detail-tone);
  }
</style>
</head>
<body>
<main class="canvas">
  <section class="card card--front" aria-label="Business card front">
    <div class="brand">
      <span class="brand__dot"></span>
      <span class="brand__name">Silver Heron Holdings, LLC</span>
    </div>
    <div class="holder">
      <p class="holder__name">John Doe</p>
      <p class="holder__role">Designation</p>
    </div>
    <div class="contact">
      <p><span class="contact__label">M:</span> +1234567890</p>
      <p><span class="contact__label">E:</span> john@silverheronholdings.com</p>
    </div>
  </section>

  <section class="card card--back" aria-label="Business card back">
    <div class="brand">
      <span class="brand__dot"></span>
      <span class="brand__name">Silver Heron Holdings, LLC</span>
    </div>
    <p class="website">www.silverheronholdings.com</p>
  </section>
</main>
</body>
</html>
```